Business Card Design for Retail Product Line

We need a two-sided, full-color business card for a new oral care product line. The feel of the card should invoke emotions of happiness and health. It should be bright, cheerful and modern in appearance. The card should be mostly matte finish, but with elements of spot-gloss and/or raised/embossed features (print, logo, tag lines, etc.).

Target Market(s)

People who are into whole-body health, eat well and understand the importance of nutrition.

Industry/Entity Type

Health And Wellness

Contact Information for Business Card

The logo, color scheme and tag-lines have all been developed and artwork is attached. Card is to be standard-sized and should use a mix of clean, sans-serif fonts; the main font (DIN) is attached as well. The card will be used for 3 individuals and should include placeholders for:
1. Name
2. Title (for example, "CEO")
3. Business address
4. Phone number
5. Website
6. Email address

Font styles to use
Sans Serif
Other font styles liked:
• DIN font

Colors
faa54b
000000
5c5c5c
a2ce44

Requirements
Must have
• 2 sides
• Full color orange on one side
• Image of DNA leaves
• Tag line "Glow from the Root Upward", on single side with orange background
• Company Logo (Plome) on same side as text (name, phone, address, etc.)
• Name, Title, Business Address, Phone Number, Website, Email address
• UPDATE: "Brisk Marrow", not "Brisk M Arrow"
Should not have
• Calligraphy
• Dark colors
• UPDATE!! Do not include "Turmeric infused toothpaste" on the business card
• UPDATE #2!! Do not include "Brisk Marrow" on the business card

```html
<!DOCTYPE html>
<html lang="en">
<head>
<meta charset="utf-8">
<title>Plome Business Card</title>
<link rel="stylesheet" href="https://fonts.googleapis.com/css2?family=Aleo:ital,wght@0,400;0,600;0,700;1,400&family=Barlow+Semi+Condensed:wght@500;600;700&display=swap">
<style>
  :root {
    --bg: #e6e6e6;
    --orange: #f9a54d;
    --orange-deep: #e0862c;
    --gold: #f2c233;
    --ink: #1c1c1c;
    --grey: #5c5c5c;
    --leaf: #a2ce44;
    --leaf-deep: #4f9a34;
    --white: #ffffff;
  }
  * { box-sizing: border-box; margin: 0; padding: 0; }
  html, body { width: 1200px; height: 1200px; overflow: hidden; background: var(--bg); }
  .canvas { position: relative; width: 1200px; height: 1200px; }

  .card { position: absolute; width: 565px; height: 314px; }

  .card-front {
    left: 320px; top: 208px; background: var(--orange);
    display: flex; flex-direction: column; align-items: center; justify-content: center; gap: 10px;
  }
  .front-wordmark { font-family: "Aleo", serif; font-weight: 700; font-size: 96px; line-height: 1; color: var(--white); letter-spacing: 1px; }
  .tagline { font-family: "Barlow Semi Condensed", sans-serif; color: var(--white); text-align: center; line-height: 1; }
  .tagline-lead { display: block; font-size: 26px; font-weight: 700; }
  .tagline-rest { display: block; font-size: 13px; font-weight: 700; letter-spacing: 1px; margin-top: 3px; }

  .card-back { left: 321px; top: 607px; background: var(--white); }
  .brand-mark {
    position: absolute; left: 82px; top: 44px; width: 78px; height: 66px;
    background: linear-gradient(115deg, var(--orange-deep) 0%, var(--gold) 45%, var(--orange-deep) 100%);
    display: flex; align-items: center; justify-content: center;
  }
  .brand-name { font-family: "Aleo", serif; font-weight: 700; font-size: 22px; color: var(--white); }

  .accent-rule {
    position: absolute; left: 172px; right: 2px; top: 107px; height: 3px;
    background: linear-gradient(90deg, var(--gold), var(--orange-deep) 35%, var(--gold) 70%, var(--orange-deep));
  }

  .dna-leaves {
    position: absolute; left: 82px; top: 228px; width: 18px; height: 43px;
    background: linear-gradient(180deg, var(--leaf) 0%, var(--leaf-deep) 45%, var(--grey) 100%);
    border-radius: 4px;
  }

  .contact { position: absolute; left: 318px; top: 145px; font-family: "Aleo", serif; }
  .contact-name { font-size: 18px; font-weight: 600; color: var(--ink); }
  .contact-title { font-size: 15px; font-style: italic; color: var(--ink); margin-top: 2px; }
  .contact-details { list-style: none; margin-top: 8px; font-size: 13px; color: var(--grey); line-height: 20px; }
</style>
</head>
<body>
<main class="canvas">
  <section class="card card-front" aria-label="Card front">
    <span class="front-wordmark">Plome</span>
    <p class="tagline">
      <span class="tagline-lead">glow</span>
      <span class="tagline-rest">FROM THE ROOT UPWARD ™</span>
    </p>
  </section>

  <section class="card card-back" aria-label="Card back">
    <div class="brand-mark"><span class="brand-name">Plome</span></div>
    <div class="accent-rule"></div>

    <div class="dna-leaves" role="img" aria-label="DNA strand with green leaves illustration"></div>

    <div class="contact">
      <p class="contact-name">Daniel Marsh</p>
      <p class="contact-title">Managing Director</p>
      <ul class="contact-details">
        <li>12 Harbor Lane, Fairview, USA</li>
        <li>T: 01 2468135</li>
        <li>W. www.plome.com</li>
        <li>E. hello@plome.com</li>
      </ul>
    </div>
  </section>
</main>
</body>
</html>
```